Business Card Design Project

Im an electrician and my company name is Brightway Electrical
My main work is installing Lighting and Power Points, Home Theater Systems, TVS, Phones and Data
Im looking a business card, something nice, clean, modern and not to cluttered
Im open to sugestions
I dont mind if the "Services" is on the back on the business card
colours black, grey, white or the blue colour of my logo are prefered but not compulsory
any questions just message me
and please make it so if i need to edit the writing can do it easy. maybe by making it a seperate layer ?
My Details are.
Name - Peter Hollis
Job Title - Licenced Electrician
Mobile - 027 530 2174
Email - peter@brightwayelectrical.co.nz
Web - www.brightwayelectrical.co.nz
Services
Residential / Commercial
Lighting & Power
Heating & Ventilation
Automation
Phone & Data
Home Cinema
Sound Systems
TV, Antenna & Satellite
Digital Upgrades

```html
<!DOCTYPE html>
<html lang="en">
<head>
<meta charset="utf-8">
<title>Brightway Electrical – Business Card</title>
<link rel="stylesheet" href="https://fonts.googleapis.com/css2?family=Arimo:wght@400;700&display=swap">
<style>
  :root {
    --brand-blue: #00b3cc;
    --panel-grey: #6b727a;
    --back-grey: #6a7079;
    --ink: #111111;
    --ink-dark: #222222;
    --paper: #ffffff;
    --edge: #333333;
    --bar-black: #161616;
    --silver-light: #f2f2f2;
    --silver-mid: #bdbdbd;
    --silver-dark: #7d7d7d;
  }
  * { margin: 0; padding: 0; box-sizing: border-box; }
  html, body {
    width: 1200px;
    height: 330px;
    overflow: hidden;
    background: var(--paper);
    font-family: "Arimo", Arial, sans-serif;
  }
  .sheet { position: relative; width: 1200px; height: 330px; }

  .card {
    position: absolute;
    top: 0;
    height: 330px;
    border: 1px solid var(--edge);
    overflow: hidden;
  }
  .card--front { left: 0; width: 511px; background: var(--paper); }
  .card--back  { left: 685px; width: 515px; background: var(--back-grey); }

  /* Front: brand */
  .brand {
    position: absolute;
    left: 30px;
    top: 14px;
    display: flex;
    align-items: center;
    gap: 10px;
  }
  .brand__mark {
    width: 40px;
    height: 40px;
    background: var(--brand-blue);
  }
  .brand__name {
    color: var(--brand-blue);
    font-weight: 700;
    font-size: 18px;
    line-height: 19px;
    letter-spacing: 0.5px;
    text-transform: uppercase;
  }

  /* Front: contact */
  .contact {
    position: absolute;
    left: 258px;
    top: 68px;
    color: var(--ink);
  }
  .contact__name { font-size: 16px; line-height: 20px; }
  .contact__title { font-size: 12px; line-height: 16px; margin-top: 2px; }
  .contact__email { font-size: 16px; line-height: 20px; margin-top: 6px; }

  /* Front: services band */
  .rail {
    position: absolute;
    left: 0;
    width: 100%;
    height: 22px;
    background: linear-gradient(to bottom,
      var(--silver-mid) 0%, var(--silver-light) 35%,
      var(--silver-mid) 65%, var(--silver-dark) 100%);
  }
  .rail--top { top: 148px; }
  .rail--bottom { top: 258px; height: 18px; }

  .services {
    position: absolute;
    left: 0;
    top: 170px;
    width: 100%;
    height: 88px;
    background: var(--panel-grey);
    padding: 7px 20px 0 26px;
    color: var(--paper);
    font-size: 17.5px;
    line-height: 25px;
  }

  .web-bar {
    position: absolute;
    left: 0;
    top: 276px;
    width: 100%;
    height: 38px;
    background: var(--bar-black);
  }
  .web-bar__url {
    position: absolute;
    right: 22px;
    top: 10px;
    color: var(--brand-blue);
    font-size: 15px;
  }

  /* Back */
  .back-brand {
    position: absolute;
    right: 28px;
    bottom: 30px;
    color: var(--brand-blue);
    font-weight: 700;
    font-size: 20px;
    line-height: 24px;
    letter-spacing: 1px;
    text-transform: uppercase;
    text-align: left;
  }
</style>
</head>
<body>
<main class="sheet">

  <section class="card card--front" aria-label="Business card front">
    <div class="brand">
      <span class="brand__mark" aria-hidden="true"></span>
      <span class="brand__name">Brightway<br>Electrical</span>
    </div>

    <div class="contact">
      <p class="contact__name">Peter Hollis&nbsp; - &nbsp;027 530 2174</p>
      <p class="contact__title">Licenced Electrician</p>
      <p class="contact__email">E- peter@brightwayelectrical.co.nz</p>
    </div>

    <div class="rail rail--top" aria-hidden="true"></div>
    <div class="services">
      <p>Residential / Commercial ▪ Lighting &amp; Power▪ Heating &amp;</p>
      <p>Ventilation ▪ Automation ▪ Phone &amp; Data ▪ Home Cinema</p>
      <p>Sound Systems ▪ TV, Antenna &amp; Satellite ▪ Digital Upgrades</p>
    </div>
    <div class="rail rail--bottom" aria-hidden="true"></div>

    <div class="web-bar">
      <span class="web-bar__url">www.brightwayelectrical.co.nz</span>
    </div>
  </section>

  <section class="card card--back" aria-label="Business card back">
    <p class="back-brand">Brightway<br>Electrical</p>
  </section>

</main>
</body>
</html>
```